I need the following on my business card:
- Name: Dana Whitcomb
- License # 0M93216
- Title: Producer
- Phone: (555) 017-3904
- Email: Dana@CorbelInsuranceServices.com

- Company: Corbel Insurance Services
- Address: 27408 Larkmoor Ave Suite 610, Alder Falls, NV 90217
- Website: www.CorbelInsuranceServices.com

Also add our slogan on the card: "Where Care Meets Protection"

```html
<!DOCTYPE html>
<html lang="en">
<head>
<meta charset="utf-8">
<title>Corbel Insurance Services – Business Card</title>
<link rel="stylesheet" href="https://fonts.googleapis.com/css2?family=Outfit:wght@400;500;600;700&family=Montserrat:ital,wght@1,400&display=swap">
<style>
  :root {
    --page-bg: #d4d5d5;
    --card-white: #f6f6f4;
    --brand-blue: #28309a;
    --brand-green: #2aa636;
    --ink: #222222;
    --white: #ffffff;
  }
  * { box-sizing: border-box; margin: 0; padding: 0; }
  html, body {
    width: 1200px; height: 1200px; overflow: hidden;
    background: var(--page-bg);
    font-family: "Outfit", sans-serif;
  }
  .canvas { position: relative; width: 1200px; height: 1200px; }
  .card {
    position: absolute; top: 466px;
    width: 488px; height: 278px;
    border-radius: 30px; overflow: hidden;
  }
  .card-front { left: 80px; background: var(--card-white); }
  .card-back { left: 635px; background: var(--brand-blue); }

  .wordmark { position: absolute; left: 0; right: 0; text-align: center; font-weight: 600; }
  .wordmark-name { display: block; font-size: 36px; letter-spacing: 1px; line-height: 1; }
  .wordmark-tag {
    display: block; font-size: 12px; font-weight: 500; letter-spacing: 4.5px;
    margin-top: 8px; line-height: 1; color: var(--brand-green);
  }
  .card-front .wordmark { top: 42px; color: var(--brand-blue); }
  .card-back .wordmark { top: 105px; color: var(--white); }
  .card-back .wordmark-name { font-size: 38px; }
  .card-back .wordmark-tag { font-size: 13px; letter-spacing: 5px; }

  .info-band {
    position: absolute; left: 0; right: 0; top: 113px; height: 113px;
    background: var(--brand-blue);
    border-top: 3px solid var(--brand-green);
    border-bottom: 3px solid var(--brand-green);
    text-align: center; color: var(--white);
  }
  .holder-name { font-size: 38px; font-weight: 500; line-height: 1; margin-top: 14px; }
  .holder-credentials { font-size: 19px; font-weight: 600; color: var(--brand-green); margin-top: 9px; line-height: 1; }
  .holder-contact { font-size: 13px; font-weight: 400; margin-top: 11px; line-height: 1; }
  .divider { margin: 0 5px; }

  .office {
    position: absolute; left: 0; right: 0; top: 240px;
    text-align: center; font-size: 13px; color: var(--ink); line-height: 15px;
  }
  .slogan {
    position: absolute; left: 0; right: 0; top: 207px;
    text-align: center; color: var(--white);
    font-family: "Montserrat", sans-serif; font-style: italic; font-size: 12.5px;
  }
</style>
</head>
<body>
<main class="canvas">
  <section class="card card-front" aria-label="Business card front">
    <div class="wordmark">
      <span class="wordmark-name">CORBEL</span>
      <span class="wordmark-tag">INSURANCE SERVICES</span>
    </div>
    <div class="info-band">
      <p class="holder-name">Dana Whitcomb</p>
      <p class="holder-credentials">License # 0M93216<span class="divider">|</span>Title: Producer</p>
      <p class="holder-contact">(555) 017-3904<span class="divider">|</span>Dana@CorbelInsuranceServices.com</p>
    </div>
    <p class="office">27408 Larkmoor Ave Suite 610, Alder Falls, NV 90217<br>www.CorbelInsuranceServices.com</p>
  </section>

  <section class="card card-back" aria-label="Business card back">
    <div class="wordmark">
      <span class="wordmark-name">CORBEL</span>
      <span class="wordmark-tag">INSURANCE SERVICES</span>
    </div>
    <p class="slogan">"Where Care Meets Protection"</p>
  </section>
</main>
</body>
</html>
```